2-Sided A4 Brochure

We're looking for a double-sided A4 brochure for print and PDF. Company is in online travel and is called "Pebble Lantern". This brochure is intended for partner organisations looking to license our technology for use on their websites. As such, the design should maintain the inspirational feel of typical travel designs whilst also conveying a good deal of professionalism.
A selection of images we've taken from the technology has be supplied along with logo and copy. Please utilise at least a few of these images in any and all designs.
Preferred colours are #56A0CD and #00286B. Copy includes headings and contact details should be in a breakout box.
Finished size: 210mm x 297mm
Bleed size (2mm): 214mm x 301mm
Safe size (5mm): 204mm x 291mm
Industry/Entity Type
Travel
Look and feel
Each slider illustrates characteristics of the customer's brand and the style your logo design should communicate.

```html
<!DOCTYPE html>
<html lang="en">
<head>
<meta charset="utf-8">
<title>Pebble Lantern – Partner Brochure</title>
<link rel="stylesheet" href="https://fonts.googleapis.com/css2?family=Delius&family=Gentium+Book+Plus:wght@400;700&display=swap">
<style>
  :root {
    --navy: #00286B;
    --sky: #56A0CD;
    --teal: #0aa3b5;
    --ink: #2a2a2a;
    --paper: #ffffff;
    --panel: #ececec;
  }
  html, body { margin: 0; padding: 0; overflow: hidden; background: var(--paper); }
  .brochure {
    position: relative;
    width: 853px;
    height: 1200px;
    overflow: hidden;
    background: var(--paper);
    font-family: "Gentium Book Plus", Georgia, serif;
    color: var(--ink);
  }
  .wave { position: absolute; left: 0; width: 853px; display: block; }
  .wave--top { top: 0; height: 110px; }
  .wave--bottom { bottom: 0; height: 230px; }

  .brand {
    position: absolute;
    left: 67px;
    top: 160px;
    margin: 0;
    display: flex;
    align-items: center;
    gap: 16px;
    font-family: "Gentium Book Plus", Georgia, serif;
    font-weight: 700;
    font-size: 52px;
    line-height: 1;
    color: var(--navy);
  }
  .brand__square {
    width: 34px;
    height: 34px;
    background: var(--sky);
    flex: none;
  }

  .headline {
    position: absolute;
    left: 56px;
    top: 312px;
    margin: 0;
    font-family: "Delius", "Comic Sans MS", cursive;
    font-weight: 400;
    color: var(--teal);
    line-height: 1;
  }
  .headline__first { display: block; font-size: 172px; }
  .headline__second { display: block; font-size: 122px; margin-top: -6px; padding-left: 4px; }
  .headline__mark {
    position: absolute;
    left: 642px;
    top: 360px;
    font-family: "Delius", "Comic Sans MS", cursive;
    font-size: 290px;
    line-height: 1;
    color: var(--teal);
  }

  .intro {
    position: absolute;
    left: 437px;
    top: 660px;
    width: 394px;
    padding: 2px 0 8px 2px;
    background: linear-gradient(90deg, var(--panel), #f6f6f6 70%, rgba(255,255,255,0));
  }
  .intro__title {
    margin: 0 0 6px;
    font-size: 17px;
    font-weight: 700;
    color: var(--navy);
  }
  .intro__copy {
    margin: 0;
    font-size: 13.6px;
    line-height: 22px;
    text-align: justify;
    color: #333;
  }

  .mail-icon { position: absolute; left: 320px; top: 792px; width: 90px; height: 90px; }

  .contact {
    position: absolute;
    left: 0;
    top: 887px;
    width: 410px;
    padding: 0 0 6px;
    text-align: right;
    background: linear-gradient(270deg, var(--panel), #f5f5f5 60%, rgba(255,255,255,0));
  }
  .contact__label {
    position: absolute;
    right: 3px;
    top: -3px;
    margin: 0;
    font-size: 16px;
    font-weight: 700;
    color: var(--navy);
  }
  .contact__list { margin: 0; padding: 32px 3px 0 0; list-style: none; }
  .contact__item { font-size: 25px; line-height: 30px; color: #222; }
  .contact__item--phone { font-size: 19px; color: #666; }
  .contact__item--phone strong { color: #222; }
</style>
</head>
<body>
<main class="brochure">
  <svg class="wave wave--top" viewBox="0 0 853 110" preserveAspectRatio="none" aria-hidden="true">
    <path d="M0 0 H853 V80 C700 30 520 8 0 20 Z" fill="var(--sky)"/>
    <path d="M360 0 H853 V60 C720 22 560 6 360 0 Z" fill="var(--navy)"/>
  </svg>

  <h1 class="brand"><span class="brand__square" aria-hidden="true"></span>PebbleLantern.com</h1>

  <h2 class="headline">
    <span class="headline__first">Pebble</span>
    <span class="headline__second">Lantern</span>
  </h2>
  <span class="headline__mark" aria-hidden="true">?</span>

  <section class="intro">
    <h3 class="intro__title">Pebble Lantern for Tourism Organizations</h3>
    <p class="intro__copy">Pebble Lantern offers travelers the most powerful and convenient way to plan and book their next fantastic getaway. Selecting from flights, hotels, tours, cruises, restaurants, activities and more, travelers can create custom itineraries complete with a personalized, full-color brochure before sharing them with friends or submitting them anonymously for quotes from hundreds of travel agents. Pebble Lantern’s industry-leading, patent-pending technology mirrors the experience of visiting the local, high-street travel agency whilst affording the privacy, convenience and power of transacting online.</p>
  </section>

  <svg class="mail-icon" viewBox="0 0 90 90" aria-hidden="true">
    <defs>
      <linearGradient id="tile" x1="0" y1="0" x2="0" y2="1">
        <stop offset="0" stop-color="#ffffff"/>
        <stop offset="1" stop-color="#cfd3d6"/>
      </linearGradient>
    </defs>
    <rect x="3" y="3" width="84" height="84" rx="14" fill="url(#tile)" stroke="#b9bec2"/>
    <rect x="16" y="26" width="58" height="38" rx="2" fill="#2f7fd1" stroke="#1a4f8f" stroke-width="2"/>
    <path d="M17 27 L45 50 L73 27" fill="none" stroke="#ffffff" stroke-width="3"/>
    <path d="M17 63 L37 44 M73 63 L53 44" fill="none" stroke="#ffffff" stroke-width="2"/>
  </svg>

  <section class="contact">
    <h3 class="contact__label">Contact Us</h3>
    <ul class="contact__list">
      <li class="contact__item">www.pebblelantern.com</li>
      <li class="contact__item">partners@pebblelantern.com</li>
      <li class="contact__item contact__item--phone">Ph: <strong>+61 2 5550 1472</strong> (Mon - Fri, 9am - 5pm)</li>
    </ul>
  </section>

  <svg class="wave wave--bottom" viewBox="0 0 853 230" preserveAspectRatio="none" aria-hidden="true">
    <path d="M0 230 C300 190 600 110 853 0 V230 Z" fill="var(--sky)"/>
    <path d="M330 230 C560 215 730 170 853 120 V230 Z" fill="var(--navy)"/>
  </svg>
</main>
</body>
</html>
```